Design a Flyer for Veridessa

A DL flyer to reach out to our target market. It will be placed next to our sample products that will be placed in hair salons, health clubs and trendy restaurants.

About our clientele:
- trendy, upmarket customers who are young professionals and into their health and fitness.

General image of our company:
- black and white.
-professional

What we needs in the brochure:
: Logo of our company
: Descriptions of the brand in general
: A few pictures of our products
: url of our website

Most information will be available on our website : [url removed, login to view]

```html
<!DOCTYPE html>
<html lang="en">
<head>
<meta charset="utf-8">
<title>Veridessa – DL Flyer</title>
<link rel="stylesheet" href="https://fonts.googleapis.com/css2?family=Questrial&family=Oswald:wght@500;700&family=Arimo:wght@400&display=swap">
<style>
  :root {
    --stage: #1e1e1e;
    --ink: #111111;
    --paper: #ffffff;
    --box-dark: #1a1a1a;
    --box-light: rgba(255,255,255,0.82);
    --photo-light: #d9d9d9;
    --photo-mid: #a9a9a9;
    --photo-dark: #242424;
  }
  * { box-sizing: border-box; margin: 0; padding: 0; }
  html, body {
    width: 970px; height: 1200px; overflow: hidden;
    background: var(--stage);
  }
  .flyer {
    position: absolute; left: 235px; top: 25px;
    width: 500px; height: 1150px;
    background: var(--paper);
    border: 7px solid var(--ink);
    overflow: hidden;
  }
  .hero {
    position: absolute; left: 0; top: 0; width: 100%; height: 770px;
    background: linear-gradient(160deg, var(--photo-light) 0%, #c4c4c4 45%, var(--photo-mid) 100%);
  }
  .brand {
    position: absolute; left: 24px; top: 6px;
    font-family: "Questrial", sans-serif; font-size: 82px; font-weight: 400; line-height: 1;
    color: var(--ink); letter-spacing: 0.5px;
  }
  .tagline {
    position: absolute; right: 20px; top: 100px;
    font-family: "Questrial", sans-serif; font-size: 28px; color: var(--ink);
  }
  .product-circle {
    position: absolute; width: 168px; height: 168px; border-radius: 50%;
    border: 5px solid var(--paper);
  }
  .product-circle.sheet { left: 44px; top: 172px; background: radial-gradient(circle at 60% 55%, #f2f2f2 0 38%, #555 70%, #222 100%); }
  .product-circle.bottle { left: 246px; top: 172px; background: radial-gradient(circle at 55% 50%, #e8e8e8 0 14%, #2a2a2a 30%, #1c1c1c 100%); }
  .story-title {
    position: absolute; left: 31px; top: 383px;
    font-family: "Oswald", sans-serif; font-weight: 700; font-size: 23px;
    letter-spacing: 0.5px; color: var(--ink);
  }
  .story-body {
    position: absolute; left: 31px; top: 424px; width: 243px;
    font-family: "Arimo", Arial, sans-serif; font-size: 17px; line-height: 23px;
    color: var(--ink); text-align: justify; hyphens: auto; -webkit-hyphens: auto;
  }
  .claim {
    position: absolute; left: 287px; width: 199px;
    text-align: center; font-family: "Oswald", sans-serif; text-transform: uppercase;
    overflow: hidden;
  }
  .claim.dark { background: var(--box-dark); color: var(--paper); }
  .claim.light { background: var(--box-light); color: var(--ink); }
  .claim .big { display: block; font-weight: 700; font-size: 40px; line-height: 1; letter-spacing: -0.5px; white-space: nowrap; }
  .claim .small { display: block; font-weight: 500; font-size: 14.5px; letter-spacing: 1.5px; margin-top: 6px; }
  .claim.one { top: 403px; height: 95px; padding-top: 14px; }
  .claim.two { top: 511px; height: 98px; padding-top: 18px; }
  .claim.two .big { font-size: 31px; letter-spacing: -1px; }
  .claim.three { top: 626px; height: 93px; padding-top: 13px; }
  .range {
    position: absolute; left: 0; top: 777px; width: 100%; height: 263px;
    background: linear-gradient(90deg, #1b1b1b 0%, var(--photo-dark) 50%, #1b1b1b 100%);
  }
  .visit {
    position: absolute; left: 18px; top: 1066px;
    font-family: "Questrial", sans-serif; font-size: 24px; font-weight: 700; color: var(--ink);
  }
  .url {
    position: absolute; left: 16px; top: 1096px;
    font-family: "Questrial", sans-serif; font-size: 37px; font-weight: 700; color: var(--ink);
    -webkit-text-stroke: 0.6px var(--ink);
  }
</style>
</head>
<body>
  <main class="flyer">
    <section class="hero" role="img" aria-label="Black and white photograph of a city building facade with windows"></section>
    <h1 class="brand">Veridessa</h1>
    <p class="tagline">Be nice to your skin</p>
    <div class="product-circle sheet" role="img" aria-label="Product information sheet on a gingham cloth"></div>
    <div class="product-circle bottle" role="img" aria-label="Small black bottle with a white label on a dark surface"></div>

    <h2 class="story-title">A TALE OF TWO MINDS</h2>
    <p class="story-body">Veridessa is founded by two Melbourne based pharmacists who are extremely passionate about skincare and producing a range of hand crafted products. Each product is made to order so that the best ingredients can be used, helping you be nice to your skin. Visit the website to discover Veridessa's full skin care range.</p>

    <div class="claim dark one"><span class="big">Freshly</span><span class="small">Made to order</span></div>
    <div class="claim light two"><span class="big">Meticulously</span><span class="small">Crafted products</span></div>
    <div class="claim dark three"><span class="big">To make</span><span class="small">Your skin smaile</span></div>

    <section class="range" role="img" aria-label="Photograph of the skincare range: two silver bottles, two black pump bottles and an open balm tin on black"></section>

    <p class="visit">Visit our website:</p>
    <p class="url">www.veridessa.com.au</p>
  </main>
</body>
</html>
```